Texas Civic Builders Summit Needs a Flyer

One-page event graphic/flyer and header needed. Logos provided.

2023 Texas Civic Builders Summit
Bold Ventures – True Accounts, True Answers, True Wins
August 10-11, 2023
San Antonio, Texas

About the Forum:
“Capital projects are full of risk. It’s not a question of eliminating risk, it’s a question of how to clearly identify it, reduce it, change it, or battle it.”
- Denise Holmgarten, Founder, U-BraMQ; San Antonio City Architect (retired)

Real Stories, Real Solutions, Real Success: U-BraMQ’s Texas Civic Builders Summit (TCBS) is designed to help you attain project success by hearing from Public Project Owners, architects, engineers, consultants, contractors, and suppliers. We are all in this together, and U-BraMQ is the organization that champions cross-collaboration and communication for project success!

For reference in design ONLY -
Here are some topic areas that bring project risks and/or rewards and that ultimately affect the Public Project Owner’s project success:

• Project Planning
• Regional Growth Shifts
• Project Funding
• Contracting
• Governmental Regulations
• Long-term COVID Impacts
• Infrastructure and Site Design
• Safety and Security
• Sustainability and Resilience
• Construction Predictability
• Leveraging Technology
• Facility Operations

Target Market(s)

Architects, Engineers, Contractors, project owners

Industry/Entity Type

Design and Construction

Requirements
Must have
• This is for a one-page (8.5x11) event graphic/flyer only - logos are provided. U-BraMQ logo, Texas Civic Builders Summit (TCBS) logo, 2023 Texas Civic Builders Summit, date, location
Nice to have
• Graphic(s) that represent the design and construction industry and the theme of this event (title, topics covered)
Should not have
• Full project description

```html
<!DOCTYPE html>
<html lang="en">
<head>
<meta charset="utf-8">
<title>2023 Texas Civic Builders Summit – Flyer</title>
<link rel="stylesheet" href="https://fonts.googleapis.com/css2?family=Open+Sans:wght@400;600;700&display=swap">
<style>
  :root {
    --green: #6c9c3a;
    --green-dark: #4f7f2a;
    --green-light: #8fbf4f;
    --navy: #233f94;
    --ink: #3f3f3f;
    --white: #ffffff;
    --list-ink: #1a1a1a;
  }
  html, body {
    margin: 0;
    padding: 0;
    overflow: hidden;
    background: var(--white);
  }
  .flyer {
    position: relative;
    width: 927px;
    height: 1200px;
    overflow: hidden;
    font-family: "Open Sans", Arial, sans-serif;
    color: var(--white);
  }
  .flyer-backdrop {
    position: absolute;
    inset: 0;
    width: 927px;
    height: 1200px;
  }
  .brand-name {
    position: absolute;
    left: 0;
    right: 0;
    top: 66px;
    margin: 0;
    text-align: center;
    font-size: 58px;
    line-height: 1;
    font-weight: 600;
    color: var(--ink);
  }
  .event-card {
    position: absolute;
    left: 42px;
    top: 306px;
    width: 482px;
    height: 114px;
    padding: 14px 22px;
    box-sizing: border-box;
    background: var(--navy);
    border-radius: 16px;
    font-size: 15px;
    line-height: 1.35;
  }
  .event-card p { margin: 0; white-space: nowrap; }
  .topics-intro {
    position: absolute;
    left: 594px;
    top: 306px;
    width: 294px;
    height: 118px;
    margin: 0;
    padding: 14px 16px;
    box-sizing: border-box;
    background: var(--white);
    border-radius: 10px;
    color: var(--navy);
    font-size: 14.5px;
    font-weight: 400;
    line-height: 1.4;
  }
  .topics-bridge {
    position: absolute;
    left: 700px;
    top: 420px;
    width: 110px;
    height: 28px;
    background: var(--white);
  }
  .topics-list {
    position: absolute;
    left: 620px;
    top: 444px;
    width: 266px;
    height: 294px;
    padding: 22px 16px;
    box-sizing: border-box;
    background: var(--white);
    border-radius: 12px;
    margin: 0;
    list-style: none;
    color: var(--list-ink);
    font-size: 14.5px;
    font-weight: 600;
    line-height: 1.44;
  }
  .topics-list li { white-space: nowrap; }
  .topics-list li::before { content: "• "; }
  .about-title {
    position: absolute;
    left: 56px;
    top: 452px;
    margin: 0;
    color: var(--navy);
    font-size: 42px;
    line-height: 1.2;
    font-weight: 400;
  }
  .about-text {
    position: absolute;
    left: 54px;
    top: 526px;
    width: 500px;
    margin: 0;
    font-size: 21px;
    line-height: 1.24;
    hyphens: auto;
  }
  .lessons-text {
    position: absolute;
    left: 54px;
    top: 822px;
    width: 540px;
    margin: 0;
    font-size: 21px;
    line-height: 1.24;
    hyphens: auto;
  }
  .site-link {
    position: absolute;
    left: 80px;
    top: 1112px;
    display: flex;
    align-items: center;
    gap: 16px;
    font-size: 27px;
  }
  .site-link svg { width: 24px; height: 24px; }
</style>
</head>
<body>
<main class="flyer">
  <svg class="flyer-backdrop" viewBox="0 0 927 1200" aria-hidden="true">
    <defs>
      <linearGradient id="fieldGreen" x1="0" y1="0" x2="0" y2="1">
        <stop offset="0" stop-color="#7aa846"/>
        <stop offset="1" stop-color="#5f8f33"/>
      </linearGradient>
      <linearGradient id="industrialTones" x1="0" y1="1" x2="1" y2="0">
        <stop offset="0" stop-color="#d99a55"/>
        <stop offset="0.5" stop-color="#8a7a6a"/>
        <stop offset="1" stop-color="#4e5a68"/>
      </linearGradient>
    </defs>
    <rect width="927" height="1200" fill="url(#fieldGreen)"/>
    <path d="M0 0 H927 V300 C820 240 760 170 600 200 C430 230 260 240 0 170 Z" fill="#ffffff"/>
    <path d="M0 170 C260 240 430 230 600 200 C760 170 820 240 927 300" fill="none" stroke="#8fbf4f" stroke-width="6"/>
    <path d="M380 220 C520 190 600 170 700 170 C800 170 860 220 927 250" fill="none" stroke="#6c9c3a" stroke-width="4"/>
    <path d="M0 808 C280 795 620 805 927 790 V1062 C620 1070 300 1062 0 1060 Z" fill="#233f94"/>
    <path d="M560 1200 C640 1060 790 930 927 830 V1200 Z" fill="url(#industrialTones)" role="img" aria-label="Photo of an industrial plant at sunset"/>
    <path d="M545 1200 C630 1055 780 925 927 815" fill="none" stroke="#ffffff" stroke-width="5"/>
  </svg>

  <header>
    <p class="brand-name">U-BraMQ</p>
  </header>

  <section class="event-card">
    <p>2023 Texas Civic Builders Summit</p>
    <p>Bold Ventures – True Accounts, True Answers, True Wins</p>
    <p>August 10-11, 2023</p>
    <p>San Antonio, Texas</p>
  </section>

  <p class="topics-intro">Here are some topic areas that bring project risks and/or rewards and that ultimately affect the Public Project Owner’s project success:</p>
  <div class="topics-bridge"></div>
  <ul class="topics-list">
    <li>Project Planning</li>
    <li>Regional Growth Shifts</li>
    <li>Project Funding</li>
    <li>Contracting</li>
    <li>Governmental Regulations</li>
    <li>Long-term COVID Impacts</li>
    <li>Infrastructure and Site Design</li>
    <li>Safety and Security</li>
    <li>Sustainability and Resilience</li>
    <li>Construction Predictability</li>
    <li>Leveraging Technology</li>
    <li>Facility Operations</li>
  </ul>

  <h1 class="about-title">About the Forum :</h1>
  <p class="about-text">Each of us have impressive stories of how, when faced with a project situation, we or our teams have overcome challenges and found project rewards through novel solutions, making lemonade out of lemons, or just taking steps forward through the muck and mire. If only we could better identify those risks in advance and be able to mitigate them early. After all, “Failure is not an option!”</p>

  <p class="lessons-text">Most of the project issues we encounter are ones we have already experienced, or ones that other Public Project Owners or their AEC teams have experienced. The thing is, we often fail to learn from those experiences, fail to act in advance to mitigate them, do not know what to do, or feel powerless to make change. Plus, new risks pop up on every project and shift from project inception through operations!</p>

  <footer class="site-link">
    <svg viewBox="0 0 24 24" aria-hidden="true">
      <circle cx="12" cy="12" r="11" fill="#ffffff"/>
      <g fill="none" stroke="#6c9c3a" stroke-width="1.5">
        <ellipse cx="12" cy="12" rx="4.5" ry="10"/>
        <path d="M2 12 H22 M4 7 H20 M4 17 H20"/>
      </g>
    </svg>
    <span>www.ubramq-events.org</span>
  </footer>
</main>
</body>
</html>
```